Travel Company is looking for a STAND OUT Business Card

I need a unique Business Card that will truly stand out. Nothing too busy. Simple is good, right? Not looking for a standard design either. No cookie cutter layout. We are a Travel Company that works more with Companies than Travelers. I had an idea to focus and emphasis on the 2 logo a bit more. This is not necessary, however thought it would look interesting. I am just looking for something interesting and a bit different. Does't have to completely off the wall crazy, just not your run of the mill business card.

Target Market(s)

Hoteliers, Resort Management, Call Centers, Executives, Travelers, Families, Businesses

Industry/Entity Type

Hospitality

Contact Information for Business Card

President/CEO - Marcus T Bellamy (title not necessary if design doesn't allow for it)
contact - (407) 555-0186
email - mbellamy@wayfarenow.example
address - 4812 Quillmore Ave #164
Orlando, FL 32804
website - www.wayfarenow.example

Font styles to use
Serif
Other font styles liked:
• Avenir Next LT Pro BOLD

Requirements
Must have
• simple look and design. Unique design
Nice to have
• I attached the 2 logo separate from the main logo. This can be used separately from the Main Logo, together with the main logo or as main logo. I included the logo font. Use it or not, designers choice.
Should not have
• cookie cutter design. Little use of red other than the logo

```html
<!DOCTYPE html>
<html lang="en">
<head>
<meta charset="utf-8">
<title>Wayfare Now – Business Card</title>
<link rel="stylesheet" href="https://fonts.googleapis.com/css2?family=Nunito+Sans:wght@700;800&display=swap">
<style>
  :root {
    --page-bg: #ffffff;
    --brand-red: #f40f0f;
    --ink: #111111;
    --paper: #ffffff;
    --trim: #9a9a9a;
  }
  html, body {
    margin: 0;
    padding: 0;
    width: 1200px;
    height: 1000px;
    overflow: hidden;
    background: var(--page-bg);
    font-family: "Nunito Sans", "Avenir Next", Arial, sans-serif;
  }
  .sheet {
    position: relative;
    width: 1200px;
    height: 1000px;
  }
  .card {
    position: absolute;
    top: 427px;
    width: 252px;
    height: 146px;
    box-sizing: border-box;
    overflow: hidden;
  }
  .card--front {
    left: 241px;
    background: var(--paper);
    outline: 1px dashed var(--trim);
    outline-offset: 0;
  }
  .card--back {
    left: 704px;
    background: var(--brand-red);
    color: var(--paper);
  }
  .trim-mark {
    position: absolute;
    background: var(--trim);
  }
  .trim-mark--h { width: 8px; height: 1px; }
  .trim-mark--v { width: 1px; height: 8px; }

  .wordmark {
    position: absolute;
    left: 0;
    right: 0;
    top: 58px;
    display: flex;
    align-items: center;
    justify-content: center;
    gap: 6px;
  }
  .wordmark__dot {
    width: 14px;
    height: 14px;
    border-radius: 50%;
    background: var(--brand-red);
  }
  .wordmark__name {
    font-weight: 800;
    font-size: 22px;
    letter-spacing: -0.5px;
    color: var(--ink);
    line-height: 1;
  }

  .back-mark {
    position: absolute;
    left: 8px;
    top: 14px;
    width: 92px;
    display: flex;
    flex-direction: column;
    align-items: center;
    gap: 8px;
  }
  .back-mark__circle {
    width: 72px;
    height: 72px;
    border-radius: 50%;
    background: var(--paper);
  }
  .back-mark__name {
    font-weight: 800;
    font-size: 12px;
    color: var(--paper);
    white-space: nowrap;
  }

  .holder-name {
    position: absolute;
    left: 106px;
    top: 48px;
    margin: 0;
    font-weight: 800;
    font-size: 15px;
    letter-spacing: 0.1px;
  }
  .contact {
    position: absolute;
    left: 108px;
    width: 130px;
    top: 88px;
    margin: 0;
    font-style: normal;
    text-align: center;
    font-weight: 700;
    font-size: 7.4px;
    line-height: 9.4px;
  }
</style>
</head>
<body>
<main class="sheet">

  <section class="card card--front" aria-label="Card front">
    <div class="wordmark">
      <span class="wordmark__dot" aria-hidden="true"></span>
      <span class="wordmark__name">Wayfare Now</span>
    </div>
  </section>

  <section class="card card--back" aria-label="Card back">
    <div class="back-mark">
      <span class="back-mark__circle" aria-hidden="true"></span>
      <span class="back-mark__name">Wayfare Now</span>
    </div>
    <h1 class="holder-name">Marcus T Bellamy</h1>
    <address class="contact">
      (407) 555-0186<br>
      mbellamy@wayfarenow.example<br>
      4812 Quillmore Ave #164<br>
      Orlando, FL 32804<br>
      www.wayfarenow.example
    </address>
  </section>

  <!-- trim marks around the back card -->
  <span class="trim-mark trim-mark--v" style="left:704px;top:417px"></span>
  <span class="trim-mark trim-mark--h" style="left:694px;top:427px"></span>
  <span class="trim-mark trim-mark--v" style="left:955px;top:417px"></span>
  <span class="trim-mark trim-mark--h" style="left:958px;top:427px"></span>
  <span class="trim-mark trim-mark--v" style="left:704px;top:575px"></span>
  <span class="trim-mark trim-mark--h" style="left:694px;top:572px"></span>
  <span class="trim-mark trim-mark--v" style="left:955px;top:575px"></span>
  <span class="trim-mark trim-mark--h" style="left:958px;top:572px"></span>

</main>
</body>
</html>
```